Mandarin tuition, language and travel services

We need a website for a new startup company, which offers Mandarin tuition, translating and interpreting, and travel services. Our company is based in Jersey, a British channel island. We would like a creative and modern professional website. Preferably with some animations. The attached is a website, which style we would prefer:
http://www.quorvabelt.net/
We have also attached our logo for your reference
We would also like to see designs using black, red and orange, which corresponds with our logo colours. The cartoon images could be travel resorts in China, and the president of China waving to the web-browsers. Of course, we wouldn't wish to restrain the designers creativity. Any creative and interesting ideas are welcomed! We look forward to hearing from you!

Target Market(s)

school children and adults

Industry/Entity Type

It Company

Number of Pages Required

3 page

Requirements
Must have
• We would prefer a small 3 pages website, if possible. The 3 pages need to be Services, News Room, and Contact us.

```html
<!DOCTYPE html>
<html lang="en">
<head>
<meta charset="utf-8">
<title>Lantern Mandarin – Mandarin tuition, language and travel services</title>
<link rel="stylesheet" href="https://fonts.googleapis.com/css2?family=Open+Sans:wght@400;600;700&family=Roboto+Condensed:wght@400;700&display=swap">
<style>
:root{
  --red:#d8262c;
  --red-dark:#b51d22;
  --orange:#f6b12b;
  --ink:#2b2b2b;
  --text:#8a8a8a;
  --muted:#b3b3b3;
  --light:#f3f3f3;
  --line:#e4e4e4;
  --footer:#30343a;
  --footer-deep:#24272b;
  --white:#ffffff;
  --sky-top:#8fd2ee;
  --sky-bottom:#d9f0f8;
}
*{box-sizing:border-box;margin:0;padding:0}
html,body{width:717px;height:1200px;overflow:hidden}
body{font-family:"Open Sans",Arial,sans-serif;color:var(--text);background:var(--white);font-size:7px;line-height:1.55}
.page{position:relative;width:717px;height:1200px;overflow:hidden}

/* header */
.site-header{position:absolute;top:0;left:0;width:717px;height:46px;background:var(--white);z-index:3;box-shadow:0 1px 2px rgba(0,0,0,.08)}
.brand{position:absolute;left:20px;top:0;width:96px;height:62px;background:var(--white);display:flex;align-items:center;gap:5px;padding:0 8px;border-radius:0 0 4px 4px;box-shadow:0 2px 3px rgba(0,0,0,.12)}
.brand-mark{width:12px;height:12px;background:var(--red);flex:none}
.brand-name{font-family:"Roboto Condensed",Arial,sans-serif;font-weight:700;font-size:15px;line-height:1;color:var(--red)}
.header-contact{position:absolute;right:22px;top:6px;display:flex;gap:14px;font-size:7px;color:var(--ink);font-weight:600}
.header-contact span{display:flex;align-items:center;gap:4px}
.dot-icon{width:11px;height:11px;border-radius:50%;background:var(--red);display:inline-flex;align-items:center;justify-content:center}
.main-nav{position:absolute;right:22px;top:25px;display:flex;gap:15px;align-items:center;font-family:"Roboto Condensed",Arial,sans-serif;font-weight:700;font-size:7.5px;color:var(--ink);letter-spacing:.2px}
.main-nav a{color:inherit;text-decoration:none;padding-bottom:4px}
.main-nav a.is-active{color:var(--red);border-bottom:2px solid var(--red)}

/* hero */
.hero{position:absolute;top:46px;left:0;width:717px;height:266px;background:linear-gradient(180deg,var(--sky-top) 0%,var(--sky-bottom) 62%,#e9c9a8 80%,#c9473c 100%)}
.slider-dots{position:absolute;left:50%;bottom:10px;transform:translateX(-50%);display:flex;gap:4px}
.slider-dots i{display:block;width:14px;height:3px;background:rgba(255,255,255,.6)}
.slider-dots i.is-current{background:var(--white)}

/* shared section titles */
.section-title{font-family:"Roboto Condensed",Arial,sans-serif;font-weight:700;font-size:17px;color:var(--ink);text-align:center;letter-spacing:.3px}
.section-title em{font-style:normal;color:var(--orange)}
.title-rule{width:30px;height:2px;background:var(--red);margin:6px auto 0}

/* welcome */
.welcome{position:absolute;top:312px;left:0;width:717px;height:252px;padding-top:20px}
.welcome .lead{width:470px;margin:12px auto 0;text-align:center;font-size:6.5px}
.services{display:flex;justify-content:center;gap:22px;margin-top:22px}
.service{width:118px}
.service-icon{height:34px;display:flex;align-items:center;justify-content:center}
.service h3{font-family:"Roboto Condensed",Arial,sans-serif;font-weight:700;font-size:9px;color:var(--ink);text-align:center;margin-top:6px}
.service p{font-size:6px;text-align:center;margin-top:4px;line-height:1.5}
.read-more{display:block;margin-top:5px;font-family:"Roboto Condensed",Arial,sans-serif;font-weight:700;font-size:6.5px;color:var(--red);text-align:center}

/* how to apply */
.apply{position:absolute;top:564px;left:0;width:717px;height:166px;background:var(--light);padding-top:28px;text-align:center}
.apply .lead{width:440px;margin:10px auto 0;font-size:6.5px}
.button{display:inline-block;margin-top:14px;background:var(--red);color:var(--white);font-family:"Roboto Condensed",Arial,sans-serif;font-weight:700;font-size:7px;padding:7px 18px;border-radius:2px;letter-spacing:.3px;box-shadow:0 2px 0 var(--red-dark)}

/* testimonials */
.testimonials{position:absolute;top:730px;left:0;width:717px;height:166px;padding-top:22px}
.testimonial{position:absolute;left:110px;top:68px;width:500px;display:flex;gap:16px;align-items:flex-start}
.client-photo{width:58px;height:58px;border-radius:50%;flex:none;background:linear-gradient(160deg,#c9cdd2,#8d949c);border:3px solid var(--white);box-shadow:0 0 0 1px var(--line)}
.quote p{font-size:6.5px;font-style:italic;line-height:1.6}
.quote cite{display:block;margin-top:5px;font-style:normal;font-family:"Roboto Condensed",Arial,sans-serif;font-weight:700;font-size:7px;color:var(--red)}
.slide-arrow{position:absolute;top:92px;width:14px;height:14px;display:flex;align-items:center;justify-content:center}
.slide-arrow.prev{left:58px}
.slide-arrow.next{right:58px}
.deco-circle{position:absolute;left:72px;top:62px;width:44px;height:44px;border-radius:50%;background:var(--light)}

/* policy band */
.policies{position:absolute;top:896px;left:0;width:717px;height:72px;background:var(--orange);display:flex;justify-content:center;gap:30px;padding-top:16px}
.policy{width:180px;display:flex;gap:9px}
.policy-icon{width:36px;height:36px;border:1.5px solid var(--white);border-radius:50%;flex:none;display:flex;align-items:center;justify-content:center}
.policy h4{font-family:"Roboto Condensed",Arial,sans-serif;font-weight:700;font-size:8px;color:var(--white);margin-top:3px}
.policy p{font-size:6px;color:var(--white);line-height:1.45;margin-top:2px}

/* footer */
.site-footer{position:absolute;top:968px;left:0;width:717px;height:210px;background:var(--footer);display:flex;padding:26px 0 0 30px;gap:0}
.footer-brand{width:210px;display:flex;align-items:flex-start;gap:6px;padding-top:2px}
.footer-brand .brand-mark{width:14px;height:14px;margin-top:2px}
.footer-brand .brand-name{font-size:19px;color:var(--red)}
.footer-col h5{font-family:"Roboto Condensed",Arial,sans-serif;font-weight:700;font-size:9px;color:var(--white);letter-spacing:.3px;margin-bottom:8px}
.footer-col ul{list-style:none}
.footer-col li{font-size:6.5px;color:#b9bcc0;line-height:1.9}
.col-info{width:110px}
.col-news{width:180px}
.col-news p{font-size:6.5px;color:#b9bcc0;line-height:1.6}
.field{margin-top:8px;width:150px;height:16px;background:var(--white);border-radius:1px;font-size:6px;color:var(--muted);padding:4px 6px}
.subscribe{display:inline-block;margin-top:6px;background:var(--red);color:var(--white);font-family:"Roboto Condensed",Arial,sans-serif;font-weight:700;font-size:6.5px;padding:4px 10px}
.col-contact li{display:flex;gap:5px;align-items:flex-start}
.col-contact li svg{flex:none;margin-top:2px}

.bottom-bar{position:absolute;top:1178px;left:0;width:717px;height:22px;background:var(--footer-deep);display:flex;align-items:center;justify-content:space-between;padding:0 24px 0 30px}
.bottom-bar small{font-size:6px;color:#8f9296}
.social{display:flex;gap:5px}
.social i{display:block;width:13px;height:13px;border-radius:50%;border:1px solid #70747a}
</style>
</head>
<body>
<div class="page">

  <header class="site-header">
    <div class="brand">
      <span class="brand-mark"></span>
      <span class="brand-name">Lantern Mandarin</span>
    </div>
    <div class="header-contact">
      <span><i class="dot-icon"><svg width="6" height="6" viewBox="0 0 10 10"><path d="M2 1l2 2-1 1.5c.6 1.2 1.4 2 2.5 2.5L7 6l2 2-1.5 1.5C4.5 9 1 5.5.5 2.5z" fill="#fff"/></svg></i>1 000 000 000</span>
      <span><i class="dot-icon"><svg width="6" height="6" viewBox="0 0 10 10"><rect x="1" y="2" width="8" height="6" fill="none" stroke="#fff" stroke-width="1.2"/><path d="M1 2l4 3 4-3" fill="none" stroke="#fff" stroke-width="1.2"/></svg></i>info@lanternmandarin.com</span>
    </div>
    <nav class="main-nav">
      <a class="is-active">HOME</a>
      <a>ABOUT US</a>
      <a>SERVICES</a>
      <a>NEWS ROOM</a>
      <a>CONTACT US</a>
      <svg width="9" height="9" viewBox="0 0 10 10"><circle cx="4" cy="4" r="3" fill="none" stroke="#2b2b2b" stroke-width="1.4"/><path d="M6.2 6.2L9 9" stroke="#2b2b2b" stroke-width="1.4"/></svg>
    </nav>
  </header>

  <section class="hero" role="img" aria-label="Illustration of Chinese pagodas, temples and a palace gate under a blue sky with an aeroplane flying overhead">
    <div class="slider-dots"><i class="is-current"></i><i></i><i></i><i></i></div>
  </section>

  <section class="welcome">
    <h1 class="section-title">WELCOME TO <em>LANTERN MANDARIN</em></h1>
    <div class="title-rule"></div>
    <p class="lead">We teach Mandarin to learners of every age in small friendly groups, with patient native tutors, clear lesson plans and regular progress reports. Alongside our classes we translate documents, interpret at meetings and plan trips across China so that every step of your journey feels simple, calm and well prepared from start to finish.</p>
    <div class="services">
      <article class="service">
        <div class="service-icon">
          <svg width="40" height="30" viewBox="0 0 40 30"><circle cx="12" cy="8" r="5" fill="#d8262c"/><path d="M3 28c0-7 4-11 9-11s9 4 9 11z" fill="#d8262c"/><circle cx="28" cy="8" r="5" fill="#2b2b2b"/><path d="M19 28c0-7 4-11 9-11s9 4 9 11z" fill="#2b2b2b"/></svg>
        </div>
        <h3>MANDARIN TUITION</h3>
        <p>Friendly group and private classes for school children and adults, from first words to exams.</p>
        <span class="read-more">READ MORE &gt;&gt;</span>
      </article>
      <article class="service">
        <div class="service-icon">
          <svg width="40" height="32" viewBox="0 0 40 32"><rect x="2" y="2" width="18" height="16" rx="2" fill="#2b2b2b"/><text x="11" y="14" font-family="Roboto Condensed, sans-serif" font-weight="700" font-size="11" fill="#fff" text-anchor="middle">A</text><rect x="18" y="13" width="18" height="16" rx="2" fill="#d8262c"/><path d="M22 18h10M27 16v10M23 25l8-5" stroke="#fff" stroke-width="1.6" fill="none"/></svg>
        </div>
        <h3>TRANSLATING</h3>
        <p>Accurate written translation of letters, contracts and study papers between English and Chinese.</p>
        <span class="read-more">READ MORE &gt;&gt;</span>
      </article>
      <article class="service">
        <div class="service-icon">
          <svg width="40" height="32" viewBox="0 0 40 32"><rect x="4" y="4" width="22" height="24" fill="none" stroke="#2b2b2b" stroke-width="2"/><path d="M9 11h12M9 16h12M9 21h7" stroke="#2b2b2b" stroke-width="1.6"/><path d="M36 6l-14 16-3 5 5-3 14-16z" fill="#d8262c"/></svg>
        </div>
        <h3>INTERPRETING</h3>
        <p>Professional interpreters for business meetings, medical visits, conferences and family events.</p>
        <span class="read-more">READ MORE &gt;&gt;</span>
      </article>
      <article class="service">
        <div class="service-icon">
          <svg width="40" height="32" viewBox="0 0 40 32"><path d="M4 18l10-1 9-12c1-2 4-2 3 1l-5 11 10-1 3-4h3l-2 7 2 7h-3l-3-4-10-1 5 11c1 3-2 3-3 1l-9-12-10-1z" fill="#d8262c"/><path d="M14 17l-4-8h3l7 8" fill="#2b2b2b"/></svg>
        </div>
        <h3>TRAVEL SERVICES</h3>
        <p>Tailored tours, flights and hotels for holidays and study trips to the best places in China.</p>
        <span class="read-more">READ MORE &gt;&gt;</span>
      </article>
    </div>
  </section>

  <section class="apply">
    <h2 class="section-title">HOW TO <em>SUBMIT YOUR APPLICATIONS</em></h2>
    <div class="title-rule"></div>
    <p class="lead">Choose the course or service you need, fill in our short online form and send it with any documents. Our team will reply within two working days with a clear quote, available dates and the next simple steps to begin.</p>
    <span class="button">CLICK HERE TO GET DETAILS &gt;&gt;</span>
  </section>

  <section class="testimonials">
    <h2 class="section-title">OUR <em>TESTIMONIALS</em></h2>
    <div class="title-rule"></div>
    <div class="deco-circle"></div>
    <span class="slide-arrow prev"><svg width="6" height="10" viewBox="0 0 6 10"><path d="M5 1L1 5l4 4" fill="none" stroke="#b3b3b3" stroke-width="1.5"/></svg></span>
    <div class="testimonial">
      <div class="client-photo" role="img" aria-label="Portrait photo of a smiling client in a suit"></div>
      <blockquote class="quote">
        <p>“My son started lessons knowing nothing at all, and after one year he can hold a real conversation. The tutors are patient and kind, the classes are fun, and when we travelled to Beijing last summer the team arranged everything for us perfectly. We could not be happier with the whole experience.”</p>
        <cite>– ALAN MARSH</cite>
      </blockquote>
    </div>
    <span class="slide-arrow next"><svg width="6" height="10" viewBox="0 0 6 10"><path d="M1 1l4 4-4 4" fill="none" stroke="#b3b3b3" stroke-width="1.5"/></svg></span>
  </section>

  <section class="policies">
    <div class="policy">
      <span class="policy-icon"><svg width="18" height="14" viewBox="0 0 18 14"><rect x="1" y="2" width="16" height="10" rx="1" fill="none" stroke="#fff" stroke-width="1.4"/><circle cx="9" cy="7" r="2.5" fill="none" stroke="#fff" stroke-width="1.2"/></svg></span>
      <div><h4>TUITION &amp; STUDY FEES</h4><p>Clear termly prices for groups and private lessons, with family discounts.</p></div>
    </div>
    <div class="policy">
      <span class="policy-icon"><svg width="18" height="14" viewBox="0 0 18 14"><rect x="1" y="2" width="16" height="10" rx="1" fill="none" stroke="#fff" stroke-width="1.4"/><path d="M1 5h16" stroke="#fff" stroke-width="2"/><path d="M4 9h4" stroke="#fff" stroke-width="1.2"/></svg></span>
      <div><h4>PAYMENT METHOD</h4><p>Pay easily by card, bank transfer or in person at our island office.</p></div>
    </div>
    <div class="policy">
      <span class="policy-icon"><svg width="16" height="16" viewBox="0 0 16 16"><path d="M13 8a5 5 0 1 1-2-4" fill="none" stroke="#fff" stroke-width="1.4"/><path d="M11 1v3.5h3.5" fill="none" stroke="#fff" stroke-width="1.4"/></svg></span>
      <div><h4>REFUND POLICY</h4><p>Full refunds on cancellations made at least fourteen days before the start.</p></div>
    </div>
  </section>

  <footer class="site-footer">
    <div class="footer-brand">
      <span class="brand-mark"></span>
      <span class="brand-name">Lantern Mandarin</span>
    </div>
    <div class="footer-col col-info">
      <h5>INFORMATION</h5>
      <ul><li>Home</li><li>About us</li><li>Services</li><li>News room</li><li>Contact us</li></ul>
    </div>
    <div class="footer-col col-news">
      <h5>NEWSLETTER</h5>
      <p>Register your email address to get the latest news and offers.</p>
      <div class="field">Email address</div>
      <span class="subscribe">SUBSCRIBE</span>
    </div>
    <div class="footer-col col-contact">
      <h5>CONTACT US</h5>
      <ul>
        <li><svg width="7" height="8" viewBox="0 0 10 12"><path d="M5 0a4 4 0 0 0-4 4c0 3 4 8 4 8s4-5 4-8a4 4 0 0 0-4-4z" fill="#d8262c"/><circle cx="5" cy="4" r="1.5" fill="#30343a"/></svg>12 Harbour Row, Suite 4,<br>St Helier, Jersey</li>
        <li><svg width="7" height="7" viewBox="0 0 10 10"><path d="M2 1l2 2-1 1.5c.6 1.2 1.4 2 2.5 2.5L7 6l2 2-1.5 1.5C4.5 9 1 5.5.5 2.5z" fill="#d8262c"/></svg>1 000 000 000</li>
        <li><svg width="7" height="7" viewBox="0 0 10 10"><path d="M2 1l2 2-1 1.5c.6 1.2 1.4 2 2.5 2.5L7 6l2 2-1.5 1.5C4.5 9 1 5.5.5 2.5z" fill="#d8262c"/></svg>1 000 000 001</li>
        <li><svg width="7" height="6" viewBox="0 0 10 8"><rect x=".5" y=".5" width="9" height="7" fill="none" stroke="#d8262c"/><path d="M.5 .5l4.5 4 4.5-4" fill="none" stroke="#d8262c"/></svg>info@lanternmandarin.com</li>
      </ul>
    </div>
  </footer>

  <div class="bottom-bar">
    <small>Copyrights ©2024, Lantern Mandarin. All rights reserved.</small>
    <div class="social"><i></i><i></i><i></i><i></i></div>
  </div>

</div>
</body>
</html>
```